Quenby New Website - Online Learning and Education

New Wordpress website for an online learning site that has courses, worksheets, quizzes, etc.
Updates

We would like something similar to this website: https://harlowtruceinstitute.example/accord-training-course/. But continue with the content of our current website: http://quenbystudyframe.example

We would like something similar to this site: https://harlowtruceinstitute.example/accord-training-course/

Coding

Coded - Design and coding required

```html
<!DOCTYPE html>
<html lang="en">
<head>
<meta charset="utf-8">
<title>Quenby – Online Learning</title>
<link href="https://fonts.googleapis.com/css2?family=Lato:ital,wght@0,400;0,700;0,900;1,400&display=swap" rel="stylesheet">
<style>
:root{
  --navy:#1c2a5c;
  --navy-deep:#0f1b3d;
  --navy-ink:#0a1430;
  --red:#c4142f;
  --red-soft:#d8283f;
  --blue:#274a9a;
  --ink:#2c2f38;
  --muted:#6b6f7a;
  --paper:#ffffff;
  --mist:#eef0f4;
  --line:#d9dce3;
}
*{box-sizing:border-box;margin:0;padding:0}
html,body{width:1200px;height:3520px;overflow:hidden}
body{font-family:"Lato",Arial,sans-serif;color:var(--ink);background:var(--paper);position:relative}
.abs{position:absolute}

/* header */
.site-header{position:absolute;left:0;top:0;width:1200px;height:100px;background:var(--paper);box-shadow:0 2px 8px rgba(0,0,0,.08);z-index:5}
.brand{position:absolute;left:150px;top:30px;display:flex;align-items:center;gap:12px}
.brand-dot{width:34px;height:34px;border-radius:50%;background:var(--navy)}
.brand-name{font-size:34px;font-weight:900;color:var(--navy);letter-spacing:1px}
.main-nav{position:absolute;left:458px;top:40px;display:flex;gap:26px}
.main-nav a{font-size:14px;font-weight:700;color:var(--navy);text-decoration:none;letter-spacing:.5px}

/* hero */
.hero{position:absolute;left:0;top:100px;width:1200px;height:580px;background:linear-gradient(90deg,#f6f4f1 0%,#efe9e2 45%,#c9b9a6 100%)}
.hero-photo{position:absolute;right:0;top:0;width:720px;height:580px;background:radial-gradient(ellipse at 60% 40%,#e7d8c6 0%,#b99c83 55%,#8c7868 100%);opacity:.9}
.hero-copy{position:absolute;left:80px;top:140px;width:380px;text-align:center}
.hero-kicker{font-size:36px;font-weight:900;color:var(--navy);letter-spacing:3px}
.hero-title{font-size:76px;font-weight:900;color:var(--navy);letter-spacing:4px;line-height:1}
.hero-text{font-size:15px;color:var(--ink);margin-top:16px;line-height:1.45}
.hero-actions{margin-top:28px;display:flex;justify-content:center;gap:16px}
.btn{display:inline-block;font-size:12px;font-weight:900;letter-spacing:.8px;padding:13px 24px;text-decoration:none;color:#fff}
.btn-navy{background:var(--navy)}
.btn-red{background:var(--red)}
.btn-outline{border:2px solid var(--ink);color:var(--ink);background:transparent;padding:10px 22px}

/* about */
.about{position:absolute;left:0;top:680px;width:1200px;height:620px;background:var(--paper)}
.about-emblem{position:absolute;left:150px;top:80px;width:300px;height:300px;border-radius:50%;background:radial-gradient(circle,#e9ebf1 0%,#cfd4df 100%);display:flex;align-items:center;justify-content:center}
.about-emblem span{font-size:40px;font-weight:900;color:var(--navy);letter-spacing:2px}
.about-copy{position:absolute;left:600px;top:170px;width:460px}
.section-title{font-size:36px;font-weight:900;color:var(--navy);letter-spacing:1px}
.section-title em{font-style:normal;color:var(--red)}
.body-text{font-size:15px;line-height:1.5;color:var(--ink);margin-top:18px}
.about-copy .btn{margin-top:24px}

/* services */
.services{position:absolute;left:0;top:1300px;width:1200px;height:800px;background:linear-gradient(180deg,#f2f3f7 0%,#e6e9f0 100%)}
.services-photo{position:absolute;left:540px;top:300px;width:660px;height:500px;background:linear-gradient(120deg,#dfe3ea 0%,#b7bfcc 45%,#5b6477 100%)}
.diamond{position:absolute;top:0;width:400px;height:400px;clip-path:polygon(50% 0,100% 50%,50% 100%,0 50%);display:flex;flex-direction:column;align-items:center;justify-content:center;text-align:center;color:#fff}
.diamond-blue{background:linear-gradient(135deg,#2e56a8,#1c2f6e)}
.diamond-red{background:linear-gradient(135deg,#e0283f,#a80f25);z-index:2}
.d-courses{left:20px}.d-worksheets{left:400px}.d-quizzes{left:780px}
.diamond svg{width:46px;height:46px;margin-bottom:10px}
.diamond h3{font-size:22px;font-weight:900;letter-spacing:1.5px}
.diamond p{font-size:12px;line-height:1.4;margin-top:6px;width:170px}
.diamond .btn{margin-top:14px;padding:7px 20px;font-size:10px;border:1px solid #fff;background:rgba(255,255,255,.1)}
.slide-arrow{position:absolute;top:184px;width:32px;height:32px;z-index:3}
.arrow-left{left:10px}.arrow-right{right:10px}
.learning-copy{position:absolute;left:168px;top:420px;width:420px}

/* testimonials */
.testimonials{position:absolute;left:0;top:2100px;width:1200px;height:440px;background:linear-gradient(100deg,var(--navy) 0%,#3a2d6a 50%,var(--red) 100%);text-align:center;color:#fff}
.testimonials h2{font-size:30px;font-weight:900;letter-spacing:1px;margin-top:80px}
.avatar{width:84px;height:84px;border-radius:50%;background:radial-gradient(circle,#d9c2b0,#8d6d5b);border:3px solid #fff;margin:22px auto 0}
.quote{font-size:18px;font-style:italic;line-height:1.45;width:720px;margin:22px auto 0}
.quote-mark{font-size:36px;font-weight:900;vertical-align:-8px}
.author{font-size:18px;margin-top:10px}
.dots{margin-top:32px;display:flex;justify-content:center;gap:10px}
.dots i{width:12px;height:12px;border-radius:50%;border:2px solid #fff}
.dots i.on{background:#fff}

/* featured */
.featured{position:absolute;left:0;top:2540px;width:1200px;height:560px;background:var(--paper)}
.featured h2{font-size:30px;font-weight:900;color:var(--red);text-align:center;margin-top:70px;letter-spacing:1px}
.course-card{position:absolute;top:128px;width:290px;height:380px;background:var(--paper);box-shadow:0 3px 14px rgba(0,0,0,.14)}
.card-1{left:135px}.card-2{left:455px}.card-3{left:775px}
.card-media{height:160px}
.card-1 .card-media{background:linear-gradient(135deg,#9aa6b3,#4e5b6d)}
.card-2 .card-media{background:linear-gradient(135deg,#c9b29d,#7e6652)}
.card-3 .card-media{background:linear-gradient(135deg,#b6c1cc,#5e6b7b)}
.card-body{padding:18px 18px 0}
.card-body h4{font-size:15px;font-weight:900;color:var(--ink);line-height:1.3}
.card-body p{font-size:13px;color:var(--muted);line-height:1.45;margin-top:10px}
.read-more{display:block;font-size:12px;font-weight:900;color:var(--ink);margin-top:18px;text-decoration:none}

/* footer */
.site-footer{position:absolute;left:0;top:3100px;width:1200px;height:350px;background:var(--navy-deep);color:#fff}
.footer-brand{position:absolute;left:170px;top:110px;width:180px;height:120px;display:flex;align-items:center;justify-content:center}
.footer-brand span{font-size:34px;font-weight:900;color:#c7cde0;letter-spacing:2px}
.footer-col{position:absolute;top:80px}
.footer-col h5{font-size:18px;font-weight:900;letter-spacing:.5px;margin-bottom:14px}
.footer-col li{list-style:none;font-size:14px;color:#d3d8e6;line-height:1.75;display:flex;align-items:center;gap:10px}
.col-links{left:386px}.col-courses{left:566px}.col-resources{left:736px}.col-social{left:890px}
.social-box{width:16px;height:16px;background:#d3d8e6}
.footer-bar{position:absolute;left:0;top:3450px;width:1200px;height:70px;background:var(--navy-ink);color:#8a92aa;font-size:13px;text-align:center;line-height:70px}
</style>
</head>
<body>

<header class="site-header">
  <div class="brand"><span class="brand-dot"></span><span class="brand-name">QUENBY</span></div>
  <nav class="main-nav">
    <a href="#">HOME</a><a href="#">ABOUT US</a><a href="#">COURSES</a><a href="#">WORKSHEET</a><a href="#">QUIZZES</a><a href="#">BLOGS</a><a href="#">CONTACT</a>
  </nav>
</header>

<section class="hero">
  <div class="hero-photo" role="img" aria-label="Photo of a smiling student writing notes beside a laptop"></div>
  <div class="hero-copy">
    <div class="hero-kicker">WELCOME TO</div>
    <div class="hero-title">QUENBY</div>
    <p class="hero-text">Pellentesque faucibus Ut accumsan ultricies elit Maecenas at justo id velit placerat mo</p>
    <div class="hero-actions">
      <a class="btn btn-navy" href="#">GET STARTED</a>
      <a class="btn btn-red" href="#">VIEW COURSES</a>
    </div>
  </div>
</section>

<section class="about">
  <div class="about-emblem"><span>QUENBY</span></div>
  <div class="about-copy">
    <h2 class="section-title">ABOUT <em>QUENBY</em></h2>
    <p class="body-text">Pellentesque faucibus Ut accumsan ultricies elit Maecenas at justo id velit placerat molestie Donec dictum lectus non odio Cras a ante vitae enim iaculis aliquam</p>
    <p class="body-text">Mauris nunc quam venenatis nec euismod sit amet egestas placerat est Pellentesque habitant</p>
    <a class="btn btn-outline" href="#">LEARN MORE</a>
  </div>
</section>

<section class="services">
  <div class="services-photo" role="img" aria-label="Photo of a woman in glasses studying at a laptop"></div>

  <svg class="slide-arrow arrow-left" viewBox="0 0 32 32"><path d="M22 4 L8 16 L22 28" fill="none" stroke="#fff" stroke-width="3"/></svg>
  <svg class="slide-arrow arrow-right" viewBox="0 0 32 32"><path d="M10 4 L24 16 L10 28" fill="none" stroke="#fff" stroke-width="3"/></svg>

  <div class="diamond diamond-blue d-courses">
    <svg viewBox="0 0 46 46" fill="none" stroke="#fff" stroke-width="2"><rect x="5" y="6" width="36" height="26"/><path d="M15 40h16M23 32v8M12 14h22M12 20h22M12 26h14"/></svg>
    <h3>COURSES</h3>
    <p>Mauris nunc quam venenatis nec euismod sit amet egestas</p>
    <a class="btn" href="#">CLICK HERE</a>
  </div>
  <div class="diamond diamond-red d-worksheets">
    <svg viewBox="0 0 46 46" fill="none" stroke="#fff" stroke-width="2"><rect x="8" y="3" width="30" height="40" rx="2"/><rect x="13" y="8" width="20" height="8"/><path d="M14 22h4M21 22h4M28 22h4M14 29h4M21 29h4M28 29h4M14 36h4M21 36h4M28 36h4"/></svg>
    <h3>WORKSHEETS</h3>
    <p>Mauris nunc quam venenatis nec euismod sit amet egestas</p>
    <a class="btn" href="#">CLICK HERE</a>
  </div>
  <div class="diamond diamond-blue d-quizzes">
    <svg viewBox="0 0 46 46" fill="none" stroke="#fff" stroke-width="2"><rect x="5" y="5" width="36" height="28"/><path d="M12 13l3 3 5-5M24 14h10M12 24l3 3 5-5M24 25h10M17 33l-4 9M29 33l4 9"/></svg>
    <h3>QUIZZES</h3>
    <p>Mauris nunc quam venenatis nec euismod sit amet egestas</p>
    <a class="btn" href="#">CLICK HERE</a>
  </div>

  <div class="learning-copy">
    <h2 class="section-title">ONLINE LEARNING</h2>
    <p class="body-text">Pellentesque faucibus Ut accumsan ultricies elit Maecenas at justo id velit placerat molestie Donec dictum lectus non odio Cras a ante</p>
    <p class="body-text">Mauris nunc quam venenatis nec euismod sit amet egestas placerat est Pellentesque habitant</p>
    <a class="btn btn-outline" href="#" style="margin-top:22px">LEARN MORE</a>
  </div>
</section>

<section class="testimonials">
  <h2>WHAT PEOPLE SAYS</h2>
  <div class="avatar" role="img" aria-label="Portrait photo of the reviewer"></div>
  <p class="quote"><span class="quote-mark">“</span> Pellentesque faucibus Ut accumsan ultricies elit Maecenas at justo id velit placerat molestie Donec dictum lectus non odio Cras a ante <span class="quote-mark">”</span></p>
  <p class="author">By Author Name</p>
  <div class="dots"><i class="on"></i><i></i><i></i></div>
</section>

<section class="featured">
  <h2>FEATURED COURSES</h2>
  <article class="course-card card-1">
    <div class="card-media" role="img" aria-label="Photo of a student using a laptop"></div>
    <div class="card-body">
      <h4>Duis non nunc Nulla rhoncus dictum metus Curabitur</h4>
      <p>Duis non nunc Nulla rhoncus dictum metus Curabitur Etiam ut lacus sit amet nunc tempor vehicula.</p>
      <a class="read-more" href="#">READ MORE</a>
    </div>
  </article>
  <article class="course-card card-2">
    <div class="card-media" role="img" aria-label="Photo of a student reading a notebook"></div>
    <div class="card-body">
      <h4>Pellentesque faucibus Ut accumsan ultricies elit</h4>
      <p>Duis non nunc Nulla rhoncus dictum metus Curabitur Etiam ut lacus sit amet nunc tempor vehicula.</p>
      <a class="read-more" href="#">READ MORE</a>
    </div>
  </article>
  <article class="course-card card-3">
    <div class="card-media" role="img" aria-label="Photo of a learner at a desk"></div>
    <div class="card-body">
      <h4>Vivamus porttitor neque at volutpat rutrum purus</h4>
      <p>Duis non nunc Nulla rhoncus dictum metus Curabitur Etiam ut lacus sit amet nunc tempor vehicula.</p>
      <a class="read-more" href="#">READ MORE</a>
    </div>
  </article>
</section>

<footer class="site-footer">
  <div class="footer-brand"><span>QUENBY</span></div>
  <div class="footer-col col-links">
    <h5>QUICK LINKS</h5>
    <ul><li>Home</li><li>About us</li><li>Our Courses</li><li>Worksheet</li><li>Quizzes</li></ul>
  </div>
  <div class="footer-col col-courses">
    <h5>COURSES</h5>
    <ul><li>Lorem ipsum</li><li>Dolor sit</li><li>Amet consecte</li><li>Tour adipiscing</li><li>Nam varius</li></ul>
  </div>
  <div class="footer-col col-resources">
    <h5>RESOURCES</h5>
    <ul><li>Testimonials</li><li>Blog</li><li>Career</li><li>FAQ</li><li>Contact Us</li></ul>
  </div>
  <div class="footer-col col-social">
    <h5>SOCIAL MEDIA</h5>
    <ul>
      <li><span class="social-box"></span>Friendwall</li>
      <li><span class="social-box"></span>Chirper</li>
      <li><span class="social-box"></span>Workline</li>
      <li><span class="social-box"></span>Snapgram</li>
    </ul>
  </div>
</footer>
<div class="footer-bar">© 2019 Company Name. All right reserved</div>

</body>
</html>
```